Buff & Gleam

polished concrete and epoxy coatings flooring company

Target Market(s)

Industrial commercial

Industry/Entity Type

Industrial flooring contractor

Contact Information for Business Card

POLISHED CONCRETE • EPOXY COATING • TERRAZZO RESTORATION • SHOT BLASTING • SURFACE PREPARATION • JOINT FILLING • TILE/ CARPET /GLUE REMOVAL

Colors
0054AA
0677BA
7BADD7
CADEEF
E8F1F8

Requirements
Must have
• email buffandgleamfloors@mailbrook.example Address 47215 Tallowmere Rd, Fraser, MI 48093. Name Ray Tulvin. Services Polished concrete- Epoxy Coatings- Terrazzo restoration-surface preparation- safety striping- joint filling- tile/ carpet/ glue removal phone number 586-700-3926 email buffandgleamfloors.example
Nice to have
• Instagram Facebook logo maybe smaller in the corner

```html
<!DOCTYPE html>
<html lang="en">
<head>
<meta charset="utf-8">
<title>Buff &amp; Gleam — Business Card</title>
<link rel="stylesheet" href="https://fonts.googleapis.com/css2?family=Oswald:wght@300;400;500;600&family=Open+Sans:ital,wght@1,400&display=swap">
<style>
  :root {
    --backdrop: #9a9a9a;
    --card-black: #1c1c1d;
    --card-blue: #2479bf;
    --accent-blue: #1f7ad0;
    --silver: #d4d4d6;
    --white: #ffffff;
  }
  * { box-sizing: border-box; margin: 0; padding: 0; }
  html, body {
    width: 1200px; height: 800px; overflow: hidden;
    background: var(--backdrop);
    font-family: "Oswald", "Arial Narrow", sans-serif;
  }
  .canvas {
    width: 1200px; height: 800px;
    display: flex; flex-direction: column; align-items: center; justify-content: center;
    gap: 30px;
  }
  .card {
    position: relative;
    width: 630px; height: 360px;
    background: var(--card-black);
    overflow: hidden;
    box-shadow: 0 10px 24px rgba(0,0,0,.25);
  }

  /* Front */
  .card-front .brand {
    position: absolute; left: 0; right: 0; top: 95px;
    text-align: center; color: var(--silver);
  }
  .card-front .brand-name {
    font-size: 64px; font-weight: 500; letter-spacing: 3px; line-height: 1;
    text-transform: uppercase;
  }
  .card-front .brand-tagline {
    margin-top: 14px;
    font-size: 17px; font-weight: 500; letter-spacing: 2.5px;
  }
  .web-row {
    position: absolute; left: 0; right: 0; bottom: 52px;
    display: flex; align-items: center; gap: 18px;
  }
  .web-row .rule { flex: 1; height: 2px; background: var(--accent-blue); }
  .web-row .web { font-size: 26px; font-weight: 300; color: var(--white); white-space: nowrap; }
  .web-row .web b { font-weight: 300; color: var(--accent-blue); }

  /* Back */
  .card-back .panels { position: absolute; inset: 0; }
  .back-brand {
    position: absolute; left: 30px; top: 26px; color: var(--white); text-align: center;
    width: 120px;
  }
  .back-brand .brand-name { font-size: 24px; font-weight: 500; letter-spacing: 1px; line-height: 1.05; }
  .back-brand .brand-tagline { font-size: 6.5px; font-weight: 500; letter-spacing: .6px; margin-top: 5px; white-space: nowrap; }
  .services {
    position: absolute; left: 34px; top: 160px; list-style: none;
    color: var(--white); font-size: 14px; font-weight: 300; line-height: 23px;
  }
  .services li { white-space: nowrap; }
  .services li::before {
    content: ""; display: inline-block; width: 5px; height: 5px; border-radius: 50%;
    background: var(--white); margin-right: 8px; vertical-align: middle;
  }
  .services b { font-weight: 500; }
  .contact {
    position: absolute; right: 34px; top: 30px; text-align: right; color: var(--white);
  }
  .contact .person { font-size: 46px; font-weight: 600; line-height: 1; text-transform: uppercase; letter-spacing: .5px; white-space: nowrap; }
  .contact .position { font-family: "Open Sans", sans-serif; font-style: italic; font-size: 16px; margin-top: 4px; }
  .contact .address { margin-top: 48px; font-size: 17px; font-weight: 300; line-height: 1.2; }
  .contact .address b { font-weight: 600; }
  .contact .phone { margin-top: 16px; font-size: 24px; font-weight: 600; line-height: 1.1; }
  .contact .email { font-size: 16px; font-weight: 300; white-space: nowrap; }
  .contact .line { display: flex; align-items: center; justify-content: flex-end; gap: 6px; }
  .contact .line svg { width: 13px; height: 13px; flex: none; }
  .socials {
    position: absolute; right: 30px; bottom: 22px; display: flex; gap: 14px;
    color: var(--white); font-size: 10px; font-weight: 300;
  }
  .socials span { display: flex; align-items: center; gap: 4px; }
  .socials i { width: 10px; height: 10px; border-radius: 50%; background: var(--white); display: inline-block; }
</style>
</head>
<body>
<main class="canvas">

  <section class="card card-front" aria-label="Business card front">
    <div class="brand">
      <div class="brand-name">Buff &amp; Gleam</div>
      <div class="brand-tagline">INNOVATIVE CONCRETE FLOORING</div>
    </div>
    <div class="web-row">
      <span class="rule"></span>
      <span class="web">www.<b>buffandgleamfloors</b>.example</span>
      <span class="rule"></span>
    </div>
  </section>

  <section class="card card-back" aria-label="Business card back">
    <svg class="panels" width="630" height="360" viewBox="0 0 630 360" aria-hidden="true">
      <defs>
        <linearGradient id="silverStripe" x1="0" y1="0" x2="0" y2="1">
          <stop offset="0" stop-color="#f2f2f2"/>
          <stop offset=".6" stop-color="#b8b8bb"/>
          <stop offset="1" stop-color="#4a4a4c"/>
        </linearGradient>
      </defs>
      <polygon points="233,0 240,0 340,360 333,360" fill="url(#silverStripe)"/>
      <polygon points="246,0 630,0 630,360 346,360" fill="#2479bf"/>
    </svg>

    <div class="back-brand">
      <div class="brand-name">BUFF<br>&amp; GLEAM</div>
      <div class="brand-tagline">INNOVATIVE CONCRETE FLOORING</div>
    </div>

    <ul class="services">
      <li>Polished <b>Concrete</b></li>
      <li><b>Epoxy</b> Coatings</li>
      <li><b>Terrazzo</b> Restoration</li>
      <li>Surface <b>Preparation</b></li>
      <li>Safety <b>Striping</b></li>
      <li><b>Joint</b> Filling</li>
      <li>Tile/ <b>Carpet</b>/ Glue Removal</li>
    </ul>

    <div class="contact">
      <div class="person">Ray Tulvin</div>
      <div class="position">Your position</div>
      <div class="address">47215 Tallowmere Rd,<br><b>Fraser, MI 48093</b></div>
      <div class="line phone">586-700-3926
        <svg viewBox="0 0 24 24" aria-hidden="true"><path fill="#fff" d="M6.6 10.8a15 15 0 0 0 6.6 6.6l2.2-2.2c.3-.3.7-.4 1-.2 1.1.4 2.3.6 3.6.6.6 0 1 .4 1 1V20c0 .6-.4 1-1 1A17 17 0 0 1 3 4c0-.6.4-1 1-1h3.5c.6 0 1 .4 1 1 0 1.3.2 2.5.6 3.6.1.3 0 .7-.2 1z"/></svg>
      </div>
      <div class="line email">buffandgleamfloors@mailbrook.example
        <svg viewBox="0 0 24 24" aria-hidden="true"><circle cx="12" cy="12" r="10" fill="none" stroke="#fff" stroke-width="2"/><path d="M2 12h20M12 2c3 3 3 17 0 20M12 2c-3 3-3 17 0 20" fill="none" stroke="#fff" stroke-width="1.6"/></svg>
      </div>
    </div>

    <div class="socials">
      <span><i></i>@buffandgleamfloors</span>
      <span><i></i>/buffandgleamfloors</span>
    </div>
  </section>

</main>
</body>
</html>
```